Redesign of an educational Eye website for Medical Students and Healthcare professionals

www.corvellelearninghub.com is an educational resource, illustrated using high quality 3D animations, for undergraduate medical students and healthcare professionals to learn about the anatomy of the human eye and associated common eye disorders.

The website was originally developed (using a Joomla template) a couple of years ago and we now want to update the brand and design of the site. Example content and animations can be found at https://www.corvellelearninghub.com/overview or https://www.corvellelearninghub.com/ocular-anatomy/orbital-anatomy

We would like a new logo and home page design (to include new colour palette, fonts and updated overall design).

The attached PowerPoint contains an example layout of the revised components we want to appear on the new Home page. We plan to have a hero panel at the top of page playing a short video of some of the animations. Similar to how this site works (www.zeptal.uk.com).

We want the new site to feel Professional, Modern and Clean and simple.

Target Market(s)

Undergraduate medical students and Healthcare Professionals

Industry/Entity Type

Medical

Logo Text

Corvelle Learning Hub

Number of Pages Required

1 page

Font styles to use
Sans Serif

Colors

Designer to choose colors to be used in the design.

```html
<!DOCTYPE html>
<html lang="en">
<head>
<meta charset="utf-8">
<title>Corvelle Learning Hub</title>
<link href="https://fonts.googleapis.com/css2?family=Lato:ital,wght@0,400;0,700;0,900;1,400&display=swap" rel="stylesheet">
<style>
:root{
  --blue:#0a55f0;
  --ink:#1d1d1f;
  --muted:#555;
  --panel:#efefef;
  --card-top:#ececec;
  --card-bottom:#e2e2e2;
  --line:#d2d2d2;
  --white:#fff;
}
*{box-sizing:border-box;margin:0;padding:0}
html,body{width:1200px;height:4082px;overflow:hidden}
body{position:relative;font-family:'Lato',sans-serif;color:var(--ink);background:var(--white)}
.abs{position:absolute}
.center{text-align:center;left:0;width:1200px}
h2{font-weight:700;font-size:32px;color:var(--ink)}

/* hero */
.hero{top:0;left:0;width:1200px;height:640px;background:radial-gradient(ellipse at 50% 55%,#b07a5c 0%,#6a4a3a 35%,#3a3432 70%,#2a2a2c 100%)}
.hero-shade{top:0;left:0;width:1200px;height:640px;background:linear-gradient(180deg,rgba(20,20,24,.45),rgba(20,20,24,.55))}
.brand{top:30px;left:98px;display:flex;align-items:center;gap:10px;color:var(--white);font-size:30px;font-weight:700}
.brand-dot{width:16px;height:16px;border-radius:50%;background:var(--white)}
.signin{top:16px;left:966px;width:114px;height:44px;border:2px solid var(--white);border-radius:22px;color:var(--white);font-size:19px;display:flex;align-items:center;justify-content:center}
.hero h1{top:270px;font-size:50px;font-weight:700;color:var(--white)}
.hero-text{top:346px;left:220px;width:760px;text-align:center;color:var(--white);font-size:21px;line-height:27px}
.btn{height:50px;border-radius:25px;font-size:20px;display:flex;align-items:center;justify-content:center;color:var(--white)}
.btn-solid{top:455px;left:212px;width:334px;background:var(--blue)}
.btn-ghost{top:455px;left:573px;width:416px;border:2px solid var(--white)}
.dots{top:580px;left:564px;display:flex;gap:8px}
.dots span{width:12px;height:12px;border-radius:50%;background:rgba(255,255,255,.55)}

/* trusted */
.trusted-label{top:673px;left:98px;width:1004px;display:flex;align-items:center;gap:18px;font-size:13px;letter-spacing:1px;color:#333}
.trusted-label i{flex:1;height:1px;background:var(--line)}
.partners{top:740px;left:200px;width:800px;display:flex;justify-content:space-between;align-items:center}
.partner{background:#cfcfcf;border-radius:6px}

/* why */
.why{top:880px;left:0;width:1200px;height:745px;background:var(--panel)}
.feature h3{font-size:26px;font-weight:700;margin-bottom:12px}
.feature .lead{font-size:15px;font-weight:700;line-height:20px;margin-bottom:16px}
.feature li{list-style:none;font-size:14px;line-height:30px;color:#333}
.feature li::before{content:"\2192";margin-right:14px}

/* modules */
.card{top:1785px;width:250px}
.card-top{height:185px;background:var(--card-top);display:flex;align-items:center;justify-content:center}
.card-body{height:155px;background:var(--card-bottom);padding:26px 18px 0;text-align:center}
.card-body h4{font-size:15px;font-weight:700;margin-bottom:10px}
.card-body p{font-size:12px;font-weight:700;line-height:17px;color:#333}
.card-more{width:96px;height:26px;margin:2px auto 0;background:var(--card-bottom);font-size:12px;font-weight:700;display:flex;align-items:center;justify-content:center}

/* team */
.member{top:2262px;width:196px;text-align:center}
.member .photo{height:218px;background:linear-gradient(160deg,#f4f4f4,#bdb8b3 60%,#4a4240)}
.member h4{margin-top:10px;font-size:15px;font-weight:700}
.member p{font-size:12px;font-style:italic;color:#444;margin-top:3px}

/* testimonial */
.quote{top:2722px;left:600px;width:448px}
.quote h4{font-size:16px;font-weight:700;margin-bottom:10px}
.quote .role{font-size:11px;font-style:italic;color:#333;margin-bottom:12px}
.quote p{font-size:13px;line-height:21px;color:#333}

/* trial */
.trial-sub{top:3070px;font-size:15px;font-weight:700}
.btn-trial{top:3113px;left:510px;width:180px;height:38px;font-size:16px;font-weight:700;border-radius:19px;background:var(--blue)}
.video{top:3190px;left:200px;width:800px;height:396px;background:linear-gradient(180deg,#2b2b2d,#5b534f 50%,#2b2b2d)}
.charity-text{top:3698px;left:220px;width:760px;text-align:center;font-size:15px;line-height:25px;color:#333}

/* footer */
.footer{top:3795px;left:0;width:1200px;height:240px;background:var(--panel)}
.footer h5{font-size:21px;font-weight:700;margin-bottom:18px}
.social li{list-style:none;display:flex;align-items:center;gap:14px;font-size:13px;margin-bottom:12px}
.social span{width:24px;height:24px;border-radius:50%;background:var(--white)}
.links li{list-style:none;font-size:13px;margin-bottom:10px}
.links li::before{content:"\203A";margin-right:14px}
.email{width:230px;height:34px;background:var(--white);font-size:12px;font-weight:700;display:flex;align-items:center;padding-left:10px;margin-bottom:10px}
.btn-sub{width:120px;height:34px;font-size:14px;font-weight:700;border-radius:17px;background:var(--blue)}
.copyright{top:4043px;font-size:12px;color:#444}
</style>
</head>
<body>

<section class="abs hero" role="img" aria-label="Hero video still of a patient during an eye examination"></section>
<div class="abs hero-shade"></div>
<div class="abs brand"><span class="brand-dot"></span>Corvelle Learning Hub</div>
<div class="abs signin">Sign in</div>
<svg class="abs" style="top:233px;left:576px" width="48" height="48" viewBox="0 0 48 48"><circle cx="24" cy="24" r="21" fill="none" stroke="#fff" stroke-width="2" opacity=".8"/><path d="M19 15l14 9-14 9z" fill="#fff" opacity=".8"/></svg>
<h1 class="abs center" style="top:270px;font-size:50px;color:#fff">Learn Faster and Smarter</h1>
<p class="abs hero-text">Corvelle Learning Hub helps Undergratuates and healthcare proffesssionals to learn or update their knowledge about the clinically relevant anatomy, ophthalmic examination techniques eye disorders of the human eye.</p>
<div class="abs btn btn-solid">Undergraduates - Learn More</div>
<div class="abs btn btn-ghost">Healthcare Professionals - Learn More</div>
<div class="abs dots"><span></span><span></span><span></span><span></span></div>

<div class="abs trusted-label"><i></i>TRUSTED ACROSS THE WORLD<i></i></div>
<div class="abs partners">
  <div class="partner" style="width:120px;height:90px"></div>
  <div class="partner" style="width:100px;height:34px"></div>
  <div class="partner" style="width:120px;height:46px"></div>
  <div class="partner" style="width:150px;height:56px"></div>
  <div class="partner" style="width:120px;height:44px"></div>
</div>

<section class="abs why"></section>
<h2 class="abs center" style="top:912px">Why Corvelle Learning Hub?</h2>
<div class="abs feature" style="top:1045px;left:196px;width:360px">
  <h3>Credible</h3>
  <p class="lead">Written and illustrated by experienced Consultant Ophthalmologists</p>
  <ul><li>Concise text and structured content</li><li>Practical clinical emphasis</li><li>Each core topic distilled to the essential learning points</li></ul>
</div>
<svg class="abs" style="top:1000px;left:636px" width="360" height="190" viewBox="0 0 360 190"><ellipse cx="174" cy="95" rx="172" ry="92" fill="#0a55f0"/><ellipse cx="182" cy="95" rx="166" ry="88" fill="#b88070" role="img" aria-label="Close-up of a red, irritated eye"/></svg>
<svg class="abs" style="top:1300px;left:152px" width="352" height="262" viewBox="0 0 352 262"><ellipse cx="174" cy="131" rx="172" ry="128" fill="#0a55f0"/><ellipse cx="182" cy="131" rx="164" ry="124" fill="#8a8580" role="img" aria-label="Eye drops being applied to an open eye"/></svg>
<div class="abs feature" style="top:1328px;left:655px;width:360px">
  <h3>Visual</h3>
  <p class="lead">Over 70 stunning 3D animations</p>
  <ul><li>Show movement around and inside the eye</li><li>Help bring key concepts to life</li><li>Lorem ipsum</li></ul>
</div>

<h2 class="abs center" style="top:1676px">Training Modules</h2>
<div class="abs card" style="left:160px">
  <div class="card-top"><svg width="56" height="66" viewBox="0 0 56 66"><path d="M4 2h34l16 16v46H4z" fill="none" stroke="#0a55f0" stroke-width="4"/><path d="M38 2v16h16" fill="none" stroke="#0a55f0" stroke-width="4"/><path d="M14 32h28M14 42h28M14 52h28" stroke="#0a55f0" stroke-width="4"/></svg></div>
  <div class="card-body"><h4>Core Principles</h4><p>Covers clinically relevant anatomy , fundamental topics and examination techniques in Ophthalmology.</p></div>
  <div class="card-more">Learn More</div>
</div>
<div class="abs card" style="left:475px">
  <div class="card-top"><svg width="66" height="44" viewBox="0 0 66 44"><path d="M2 22C14 4 52 4 64 22C52 40 14 40 2 22z" fill="#0a55f0"/><circle cx="33" cy="22" r="12" fill="#ececec"/><circle cx="33" cy="22" r="7" fill="#0a55f0"/></svg></div>
  <div class="card-body"><h4>Ophthalmology in Practice</h4><p>Deals with common eye disorders regularly encountered by healthcare professionals.</p></div>
  <div class="card-more">Learn More</div>
</div>
<div class="abs card" style="left:790px">
  <div class="card-top"><svg width="60" height="60" viewBox="0 0 60 60"><path d="M30 2L58 20v38H2V20z" fill="#0a55f0"/><path d="M8 22l22 16 22-16" fill="none" stroke="#ececec" stroke-width="4"/></svg></div>
  <div class="card-body"><h4>AN Other</h4><p>Lorem ipsum, lorem ipsum, lorem ipsum, lorem ipsum, lorem ipsum, lorem ipsum, lorem ipsum.</p></div>
  <div class="card-more">Learn More</div>
</div>

<h2 class="abs center" style="top:2182px">Meet the team</h2>
<div class="abs member" style="left:150px"><div class="photo" role="img" aria-label="Portrait of Tomas Ridley"></div><h4>Tomas Ridley</h4><p>Consultant Ophthalmologist</p></div>
<div class="abs member" style="left:385px"><div class="photo" role="img" aria-label="Portrait of Rafael Ondera"></div><h4>Rafael Ondera</h4><p>Consultant Ophthalmologist</p></div>
<div class="abs member" style="left:615px"><div class="photo" role="img" aria-label="Portrait of Owen Marsh"></div><h4>Owen Marsh</h4><p>CTO</p></div>
<div class="abs member" style="left:848px"><div class="photo" role="img" aria-label="Portrait of Dario Kellan"></div><h4>Dario Kellan</h4><p>CTO</p></div>

<h2 class="abs center" style="top:2604px;font-size:30px">What people are saying about Corvelle Learning Hub?</h2>
<svg class="abs" style="top:2716px;left:152px" width="270" height="228" viewBox="0 0 270 228"><ellipse cx="132" cy="114" rx="130" ry="110" fill="#0a55f0"/><ellipse cx="138" cy="116" rx="126" ry="106" fill="#c9c6c2" role="img" aria-label="Portrait of the reviewing consultant"/></svg>
<div class="abs quote">
  <h4>Mr Alan Verrow MB ChB FRCOphth</h4>
  <p class="role">Consultant Ophthalmologist and Head of the School of Ophthalmology, Northvale Deanery HEWR</p>
  <p>What sets this website apart are the superb 3D animations which enhance the accompanying text more effectively than clinical videos or photographs. I would whole heartedly recommend it to medical students, optometrists, GP's, casualty doctors and ophthalmic nurse practitioners, both as an introduction to ophthalmology, but also to refresh their knowledge of core ophthalmic examination techniques and conditions.</p>
</div>

<h2 class="abs center" style="top:3020px">Want to try Corvelle Learning Hub for free?</h2>
<p class="abs center trial-sub">No credit card details required. It's completely free for 7 days</p>
<div class="abs btn btn-trial">Start Free Trial</div>
<div class="abs video" role="img" aria-label="Video still of a pair of eyes from the 3D animations"></div>
<svg class="abs" style="top:3330px;left:542px" width="116" height="116" viewBox="0 0 116 116"><circle cx="58" cy="58" r="55" fill="none" stroke="#fff" stroke-width="3" opacity=".75"/><path d="M46 36l34 22-34 22z" fill="#fff" opacity=".75"/></svg>

<h2 class="abs center" style="top:3628px">We give 10% of our profits to charity</h2>
<p class="abs charity-text">We believe it is important to give something back so from 2018 we will donate 10% of every subscription to a selected charity somewhere in the world which works to help prevent sight loss and treat eye diseases.</p>

<footer class="abs footer"></footer>
<div class="abs" style="top:3830px;left:98px">
  <h5>Community</h5>
  <ul class="social"><li><span></span>Feedwall</li><li><span></span>Chirper</li><li><span></span>Linkfolio</li></ul>
</div>
<div class="abs" style="top:3830px;left:335px">
  <h5>Newsletter</h5>
  <div class="email">Enter Email id</div>
  <div class="btn btn-sub">Subscribe</div>
</div>
<div class="abs" style="top:3830px;left:678px">
  <h5>Company</h5>
  <ul class="links"><li>About</li><li>Blog</li></ul>
</div>
<div class="abs" style="top:3830px;left:962px">
  <h5>Policies</h5>
  <ul class="links"><li>Terms of Use</li><li>Privacy and Cookies</li></ul>
</div>
<p class="abs center copyright">© 2018 &nbsp;|&nbsp; www.companyname.com</p>

</body>
</html>
```